Packaging design for Hamper boxes

We need to revamp our gift box packaging for our Hamper business. Our business Velvet Baskets (www.velvetbaskets-example.com.au) is a website that curates, packages and delivers hampers for both consumers and corporates. We do everything from champagne and gourmet treats to pamper hampers, baby hampers and beer hampers. Our typical market is 35 - 65 years who are primarily women buying gift hampers for birthdays, thankyous, celebrations, births, sympathy, isolation/care hampers or just to say ' I'm thinking of you'.

We have recently purchased the business so it is going through a bit of a transformation and we want our packaging to be cost effective as we get 1000s of each type of hamper box produced each year. The design will need to be adapted across our box range.

Hampers are a luxury gift and are seen as being special and are designed to make the recipient go ''wow'' and our packaging needs to reflect this.

I will attach the specifics of the box in terms of measurements, must haves, design specifics and brand colours etc.

Target Market(s)

Our typical market is 35 - 65 years who are primarily women buying gift hampers for birthdays, thankyous, celebrations, births, sympathy, isolation/care hampers or just to say ' I'm thinking of you'. Hampers are not a cheap gift so the people who buy hampers have higher disposable income

Font styles to use
Sans Serif
Script
Other font styles liked:
• Rylan regular for logo

Requirements
Must have
• - The hamper box MUST exude quality and a WOW factor
- Colours and logos are listed in the attached brief.
- Box in a dark grey colour (not black).
- Colour grey can vary to that detailed in brief
- Fixed ribbon (orange colour) to front of box design with our logo on ribbon (photo ref 1)
- The word ‘’Happiness’’ to be printed in a script typeface across the front of the box as per photo ref 2. Feel free to choose a different typeface, I don’t particularly like this one on the reference.
- Wording inside the box lid " Enjoy this box full of happiness"
- Please do a version that has a design treatment on the front as well the plain grey with 'Happiness' on it

```html
<!DOCTYPE html>
<html lang="en">
<head>
<meta charset="utf-8">
<title>Velvet Baskets – Hamper Box Dieline</title>
<link href="https://fonts.googleapis.com/css2?family=Great+Vibes&family=Open+Sans:wght@400;600&display=swap" rel="stylesheet">
<style>
  :root {
    --paper: #ffffff;
    --box-outside: #6e6c6a;
    --box-outside-pattern: #757371;
    --box-inside: #2d2d2d;
    --box-inside-pattern: #323232;
    --fold-outside: #5c5a58;
    --fold-inside: #3a3a3a;
    --ribbon: #e89331;
    --tie: #ffffff;
    --brand-text: #ffffff;
    --label: #111111;
  }
  html, body {
    margin: 0;
    padding: 0;
    overflow: hidden;
    background: var(--paper);
  }
  .dieline-sheet {
    display: block;
    width: 1200px;
    height: 781px;
  }
  .side-label {
    font-family: "Open Sans", sans-serif;
    font-size: 13px;
    fill: var(--label);
  }
  .outside-face { fill: var(--box-outside); }
  .outside-pattern { fill: var(--box-outside-pattern); }
  .inside-face { fill: var(--box-inside); }
  .inside-pattern { fill: var(--box-inside-pattern); }
  .fold-outside { stroke: var(--fold-outside); stroke-width: 0.8; stroke-dasharray: 3 2; fill: none; }
  .fold-inside { stroke: var(--fold-inside); stroke-width: 0.8; stroke-dasharray: 3 2; fill: none; }
  .ribbon { fill: var(--ribbon); }
  .ribbon-tie { stroke: var(--tie); stroke-width: 3; stroke-linecap: round; }
  .brand-name {
    font-family: "Open Sans", sans-serif;
    font-weight: 600;
    font-size: 21px;
    letter-spacing: 0.5px;
    fill: var(--brand-text);
  }
  .script-happiness {
    font-family: "Great Vibes", cursive;
    font-size: 30px;
    fill: var(--ribbon);
  }
  .lid-message {
    font-family: "Great Vibes", cursive;
    font-size: 19px;
    fill: var(--ribbon);
  }
</style>
</head>
<body>
<svg class="dieline-sheet" viewBox="0 0 1200 781" xmlns="http://www.w3.org/2000/svg">

  <text class="side-label" x="45" y="27">outside</text>
  <g class="box-outside">
    <rect class="outside-face" x="45" y="40" width="503" height="402"/>
    <rect class="outside-face" x="145.5" y="442" width="302.5" height="303"/>
    <g role="img" aria-label="Tonal repeat pattern of gift, champagne bottle and eye mask icons">
      <rect class="outside-pattern" x="45" y="40" width="503" height="102"/>
      <rect class="outside-pattern" x="45" y="142" width="100.5" height="201"/>
      <rect class="outside-pattern" x="448" y="142" width="100" height="201"/>
      <rect class="outside-pattern" x="45" y="343" width="503" height="99"/>
      <rect class="outside-pattern" x="145.5" y="442" width="302.5" height="303"/>
    </g>
    <path class="fold-outside" d="M45 142H548M45 343H548M145.5 40V442M448 40V442M145.5 643.5H448"/>

    <line class="ribbon-tie" x1="270" y1="106.5" x2="323" y2="106.5"/>
    <polygon class="ribbon" points="285,104 312,104 312,198 298.5,187 285,198"/>

    <text class="brand-name" x="297" y="540" text-anchor="middle">Velvet Baskets</text>
    <text class="script-happiness" x="297" y="584" text-anchor="middle">Happiness</text>

    <line class="ribbon-tie" x1="272" y1="725" x2="325" y2="725"/>
    <polygon class="ribbon" points="285,723 312,723 312,748 298.5,737 285,748"/>
  </g>

  <text class="side-label" x="667" y="36">inside</text>
  <g class="box-inside">
    <rect class="inside-face" x="667" y="49" width="503" height="402"/>
    <rect class="inside-face" x="767" y="451" width="302" height="301"/>
    <rect class="inside-pattern" x="767" y="149" width="302" height="201"
          role="img" aria-label="Tonal repeat pattern of gift, champagne bottle and eye mask icons"/>
    <path class="fold-inside" d="M667 149H1170M667 350H1170M767 49V451M1069 49V451M767 652H1069"/>

    <line class="ribbon-tie" x1="897" y1="106.5" x2="950" y2="106.5"/>
    <polygon class="ribbon" points="910,104 937,104 937,198 923.5,187 910,198"/>

    <text class="lid-message" x="917" y="559" text-anchor="middle"
          transform="rotate(180 917 559)">A box of happiness by Velvet Baskets</text>

    <line class="ribbon-tie" x1="899" y1="725" x2="952" y2="725"/>
    <polygon class="ribbon" points="910,723 937,723 937,748 923.5,737 910,748"/>
  </g>
</svg>
</body>
</html>
```